College presentation for a startup bootcamp - how to talk to customers

I need a simple design for a college PowerPoint/ google slide presentation for students that are going through a Startup BootCamp. No flashy colors
- Accessible font - or provide the font - I like the tovra's website font or normal text font
- use a neutral colors schemes of grays - with 1-2 highlight colors
- You can use the photos in the presentation or others
- Urgent the presentation is on Thursday - I will award the winner on Wednesday.
- It's 23 slides long.

Target Market(s)

College students interested in startups

Industry/Entity Type

College

Font styles to use
Serif
Sans Serif
Other font styles liked:
• helvetica

Colors

Designer to choose only greyscale colors for use in the design.

Requirements
Must have
• clean , simple design neural colors like greyscale with 1-3 pop colors
Should not have
• no flashy colors, or hard to read text

```html
<!DOCTYPE html>
<html lang="en">
<head>
<meta charset="utf-8">
<title>Customer Development – How to talk to customers</title>
<link href="https://fonts.googleapis.com/css2?family=Montserrat:wght@300;400;500&family=Open+Sans:ital,wght@0,400;0,600;0,700;1,400;1,600&display=swap" rel="stylesheet">
<style>
  :root{
    --page:#efefef;
    --slide:#f4f4f4;
    --card:#ffffff;
    --ink:#1d1d1f;
    --ink-soft:#4a4a4a;
    --muted:#8a8a8a;
    --blue:#0a5ae6;
    --blue-link:#1f64d8;
    --red:#e0201b;
    --line:#d6d6d6;
  }
  *{box-sizing:border-box;margin:0;padding:0}
  html,body{width:1200px;height:3115px;overflow:hidden;background:var(--page)}
  body{position:relative;font-family:"Open Sans",Helvetica,Arial,sans-serif;color:var(--ink)}

  /* ---------- hero ---------- */
  .hero{position:absolute;left:0;top:0;width:1200px;height:900px}
  .hero svg{position:absolute;left:0;top:0}
  .hero-title{position:absolute;left:0;width:1200px;top:326px;text-align:center;font-family:"Montserrat",sans-serif;font-weight:400;font-size:76px;color:#fff;letter-spacing:.5px}
  .hero-sub{position:absolute;left:0;width:1200px;top:458px;text-align:center;font-family:"Montserrat",sans-serif;font-weight:400;font-size:38px;color:#fff}
  .hero-rule{position:absolute;left:324px;top:525px;width:553px;height:4px;background:var(--blue)}
  .hero-author{position:absolute;left:0;width:1200px;top:684px;text-align:center;color:#fff;font-family:"Open Sans",sans-serif}
  .hero-author .name{font-size:26px;line-height:32px}
  .hero-author .role,.hero-author .mail{font-size:17px;line-height:19px;color:#f2f2f2}
  .hero-wave{z-index:2}

  /* ---------- slides ---------- */
  .slide{position:absolute;width:541px;height:305px;background:var(--slide);box-shadow:0 2px 8px rgba(0,0,0,.12);overflow:hidden}
  .col-l{left:36px}.col-r{left:623px}
  .row-1{top:981px}.row-2{top:1324px}.row-3{top:1666px}.row-4{top:2009px}.row-5{top:2351px}.row-6{top:2694px}
  .abs{position:absolute}
  .brand{position:absolute;right:44px;top:11px;font-size:8px;font-weight:600;color:var(--ink);display:flex;align-items:center;gap:3px}
  .brand i{width:6px;height:6px;border-radius:50%;background:var(--blue);display:block}
  .slide-title{position:absolute;left:48px;top:36px;font-family:"Montserrat",sans-serif;font-weight:400;font-size:20px;color:var(--ink);letter-spacing:-.3px;white-space:nowrap}
  .slide-title::after{content:"";position:absolute;left:0;top:30px;width:42px;height:2px;background:var(--blue)}
  .slide-title .hl{color:var(--blue)}
  .page-no{position:absolute;right:42px;bottom:12px;font-size:8px;font-weight:600;color:var(--ink)}
  .photo{position:absolute}

  .checklist{list-style:none}
  .checklist li{position:relative;padding-left:16px}
  .checklist li::before{content:"";position:absolute;left:0;top:4px;width:6px;height:6px;border:1px solid currentColor;box-shadow:1px 1px 0 currentColor}
  .checklist li.sub{padding-left:30px}
  .checklist li.sub::before{left:14px;width:4px;height:4px;box-shadow:none}

  /* title slide */
  .mini-title{position:absolute;left:0;width:541px;top:120px;text-align:center;font-family:"Montserrat",sans-serif;font-weight:400;font-size:30px;color:#fff}
  .mini-sub{position:absolute;left:0;width:541px;top:172px;text-align:center;font-family:"Montserrat",sans-serif;font-weight:400;font-size:14px;color:#fff}
  .mini-rule{position:absolute;left:165px;top:196px;width:211px;height:2px;background:var(--blue)}
  .mini-author{position:absolute;left:0;width:541px;top:261px;text-align:center;color:#fff;font-size:10px;line-height:11px}
  .mini-author small{display:block;font-size:5.5px;line-height:7px}

  /* agenda */
  .agenda-title{position:absolute;left:324px;top:44px;font-family:"Montserrat",sans-serif;font-size:25px;font-weight:500}
  .agenda-title::after{content:"";position:absolute;left:0;top:40px;width:40px;height:2px;background:var(--blue)}
  .agenda-lead{position:absolute;left:330px;top:103px;font-size:12px;font-weight:600;color:var(--ink-soft)}
  .agenda-list{position:absolute;left:350px;top:137px;list-style:none;font-size:9.5px;color:var(--ink-soft)}
  .agenda-list li{height:30.5px}

  /* process diagram area */
  .process-diagram{position:absolute;left:112px;top:83px;width:340px;height:180px}
  .diagram-credit{position:absolute;left:287px;top:263px;font-size:4.5px;font-weight:700;color:#555;white-space:nowrap}

  /* nice people */
  .nice-copy{position:absolute;left:48px;top:112px;width:225px;font-size:12px;line-height:15px}
  .nice-copy .red{color:var(--red);font-weight:700}
  .nice-copy .blue{color:var(--blue);font-weight:700}
  .nice-copy .bad{color:var(--red);font-weight:700;font-size:12.5px;display:block;margin-top:9px}
  .nice-copy .eg{display:block;text-align:center;margin-top:9px}
  .nice-copy .problem{display:block;text-align:center;font-weight:700;margin-top:9px}

  /* dialog lists */
  .say-list{position:absolute;left:232px;top:78px;width:266px;font-size:10.5px;line-height:15px;color:var(--ink-soft)}
  .say-list .dots::before{top:5px;width:4px;height:4px;box-shadow:none}
  .think-list{position:absolute;left:48px;top:77px;width:455px;font-size:8.3px;line-height:11.2px;color:var(--ink-soft)}
  .think-list li{padding-left:26px;margin-bottom:5.2px}
  .think-list li.hl{color:var(--blue-link);font-weight:700}
  .right-lead{position:absolute;left:48px;top:95px;font-size:8.5px;color:var(--ink-soft)}
  .right-list{position:absolute;left:48px;top:108px;font-size:8.5px;line-height:16.5px;color:var(--blue-link)}
  .right-list li.plain{color:var(--ink-soft)}

  /* rule of thumb */
  .thumb-bar{position:absolute;left:46px;width:451px;height:51px;background:var(--card);border-left:3px solid #cfcfcf;display:flex;align-items:center;font-size:13px;font-weight:700}
  .thumb-bar svg{margin:0 18px 0 22px}

  /* question cards */
  .qcard{position:absolute;width:219px;background:var(--card);padding:7px 9px;font-size:9.5px;line-height:12px;color:var(--ink-soft)}
  .qhead{position:absolute;font-size:10px;font-weight:700}
  .qhead.good{color:var(--blue)}
  .qhead::after{content:"";position:absolute;left:-9px;top:15px;width:219px;height:3px;background:var(--ink)}
  .qhead.good::after{background:var(--blue)}
  .qcard .checklist li{margin-bottom:5px}
  .qcard p{margin-bottom:6px}
  .qcard .tiny{font-size:6px;line-height:8px;margin-bottom:0}
  .qcard strong{color:var(--ink);display:block;margin:2px 0 3px}

  /* mistakes */
  .mistake-copy{position:absolute;font-size:9.5px;line-height:12px;color:var(--ink-soft);width:215px}
  .mistake-copy .cap{font-size:9px;text-transform:uppercase;letter-spacing:.2px}
  .mistake-copy b{color:var(--ink)}
  .mistake-copy em{font-weight:600;color:var(--ink)}
  .mistake-copy p{margin-bottom:12px}
</style>
</head>
<body>

<!-- ============ HERO ============ -->
<section class="hero">
  <svg width="1200" height="900" viewBox="0 0 1200 900">
    <defs>
      <radialGradient id="crowd" cx="50%" cy="40%" r="75%">
        <stop offset="0" stop-color="#a07a62"/>
        <stop offset=".45" stop-color="#5c4438"/>
        <stop offset="1" stop-color="#2b2220"/>
      </radialGradient>
    </defs>
    <path role="img" aria-label="Photo: a woman raising her hand in front of a large concert crowd" fill="url(#crowd)"
      d="M0,0 H1200 V641 C900,700 600,790 363,800 C230,795 100,770 0,756 Z"/>
  </svg>
  <h1 class="hero-title">Customer Development</h1>
  <p class="hero-sub">Mom’s test - how to talk to customers</p>
  <div class="hero-rule"></div>
  <div class="hero-author">
    <div class="name">Mara Velen</div>
    <div class="role">Co-Founder Brightstep Learning</div>
    <div class="mail">mara.velen@mailbox.test</div>
  </div>
  <svg class="hero-wave" width="1200" height="900" viewBox="0 0 1200 900">
    <path fill="var(--blue)" d="M363,800 C600,790 900,700 1200,641 V847 C1050,880 900,900 780,890 C600,875 480,830 363,800 Z"/>
  </svg>
</section>

<!-- ============ 1 title ============ -->
<section class="slide col-l row-1">
  <svg class="photo" width="541" height="305" role="img" aria-label="Photo: a woman raising her hand in front of a concert crowd">
    <defs>
      <radialGradient id="crowd2" cx="50%" cy="40%" r="75%">
        <stop offset="0" stop-color="#a07a62"/><stop offset=".5" stop-color="#5c4438"/><stop offset="1" stop-color="#2b2220"/>
      </radialGradient>
    </defs>
    <rect width="541" height="305" fill="url(#crowd2)"/>
  </svg>
  <h2 class="mini-title">Customer Development</h2>
  <p class="mini-sub">Mom’s test - how to talk to customers</p>
  <div class="mini-rule"></div>
  <div class="mini-author">Mara Velen<small>Co-Founder Brightstep Learning<br>mara.velen@mailbox.test</small></div>
</section>

<!-- ============ 2 agenda ============ -->
<section class="slide col-r row-1">
  <svg class="photo" style="left:45px;top:0" width="225" height="305" role="img" aria-label="Photo: a smiling woman holding colourful shopping bags">
    <defs><linearGradient id="shop" x1="0" y1="0" x2="0" y2="1"><stop offset="0" stop-color="#9b8a80"/><stop offset=".55" stop-color="#5e4a44"/><stop offset="1" stop-color="#7fa66a"/></linearGradient></defs>
    <rect width="225" height="305" fill="url(#shop)"/>
  </svg>
  <div class="brand"><i></i>Brightstep Learning</div>
  <h2 class="agenda-title">Agenda</h2>
  <p class="agenda-lead">Mom’s test:</p>
  <ol class="agenda-list">
    <li>1.&nbsp;&nbsp;&nbsp;What is the problem?</li>
    <li>2.&nbsp;&nbsp;&nbsp;How to talk to customers ?</li>
    <li>3.&nbsp;&nbsp;&nbsp;How to ask questions?</li>
    <li>4.&nbsp;&nbsp;&nbsp;Who to talk to?</li>
  </ol>
  <div class="page-no">Page &nbsp;|&nbsp; 2</div>
</section>

<!-- ============ 3 customer development ============ -->
<section class="slide col-l row-2">
  <div class="brand"><i></i>Brightstep Learning</div>
  <h2 class="slide-title">Customer Development</h2>
  <svg class="process-diagram" width="340" height="180" role="img" aria-label="Hand-drawn diagram of the four customer development stages: discovery, validation, creation and company building, with a pivot loop">
    <defs><linearGradient id="diagram" x1="0" y1="0" x2="1" y2="1"><stop offset="0" stop-color="#e6eefc"/><stop offset="1" stop-color="#cddcf7"/></linearGradient></defs>
    <rect width="340" height="180" fill="url(#diagram)"/>
  </svg>
  <p class="diagram-credit">Tom Arlen's Customer Development by Lio Marsh; custpath.test</p>
  <div class="page-no">Page &nbsp;|&nbsp; 3</div>
</section>

<!-- ============ 4 people try to be nice ============ -->
<section class="slide col-r row-2">
  <div class="brand"><i></i>Brightstep Learning</div>
  <h2 class="slide-title">People try to be nice ,...</h2>
  <div class="nice-copy">
    …therefore they <span class="red">lie</span> in your face <span class="blue">without realizing</span> it
    <span class="bad">Bad data it worse than no data</span>
    <span class="eg">E.g. <i>“I’ll definitely buy that”</i></span>
    <span class="problem">THE PROBLEM</span>
  </div>
  <svg class="photo" style="left:288px;top:69px" width="208" height="202" role="img" aria-label="Photo: a smiling young woman with glasses on a yellow background">
    <defs><radialGradient id="nice" cx="50%" cy="50%" r="60%"><stop offset="0" stop-color="#c89a6a"/><stop offset=".6" stop-color="#e6c14a"/><stop offset="1" stop-color="#f2cf5c"/></radialGradient></defs>
    <rect width="208" height="202" fill="url(#nice)"/>
  </svg>
  <div class="page-no">Page &nbsp;|&nbsp; 4</div>
</section>

<!-- ============ 5 what people say ============ -->
<section class="slide col-l row-3">
  <div class="brand"><i></i>Brightstep Learning</div>
  <h2 class="slide-title">Mom’s test &nbsp;- What people say</h2>
  <svg class="photo" style="left:50px;top:76px" width="146" height="196" role="img" aria-label="Photo: a woman in a patterned blouse talking and gesturing">
    <defs><linearGradient id="say" x1="0" y1="0" x2="0" y2="1"><stop offset="0" stop-color="#dedbd6"/><stop offset=".5" stop-color="#9a8576"/><stop offset="1" stop-color="#3b3a38"/></linearGradient></defs>
    <rect width="146" height="196" fill="url(#say)"/>
  </svg>
  <ul class="checklist say-list">
    <li>You: Mom, I have a business idea. Do you have 5 mins?</li>
    <li>Mom: Of course, dear</li>
    <li class="sub dots">…</li>
    <li>You: You life your tablet and use it a lot?</li>
    <li>Mom: Sure it’s great.</li>
    <li class="sub dots">…</li>
    <li>You: Would you buy a cookbook app?</li>
    <li>Mom: I love cookbooks, sounds nice. Does it come with vegan recipes? Or something special for Xmas?</li>
    <li class="sub dots">…</li>
  </ul>
  <div class="page-no">Page &nbsp;|&nbsp; 5</div>
</section>

<!-- ============ 6 what people think ============ -->
<section class="slide col-r row-3">
  <div class="brand"><i></i>Brightstep Learning</div>
  <h2 class="slide-title">Mom’s test &nbsp;- What people <span class="hl">think</span></h2>
  <ul class="checklist think-list">
    <li>You: Mom, I have a business idea. Do you have 5 mins?</li>
    <li>Mom: Of course, dear</li>
    <li class="hl">I’m proud of you and I don’t want to hurt your feelings</li>
    <li>You: You life your tablet and use it a lot?</li>
    <li>Mom: Sure it’s great.</li>
    <li class="hl">I use it to check email on the sofa</li>
    <li>You: Would you buy a cookbook app?</li>
    <li>Mom: I love cookbooks, sounds nice. Does it come with vegan recipes? Or something special for Xmas?</li>
    <li class="hl">Well, I have plenty of cookbooks. I don’t need a computer in my kitchen - it might get dirty! But hey, if my kid made it, I’ll try it. App? I never bought an app. Don’t you need to enter your credit card for that? Let me try to change the subject.</li>
  </ul>
  <div class="page-no">Page &nbsp;|&nbsp; 6</div>
</section>

<!-- ============ 7 how to do it right ============ -->
<section class="slide col-l row-4">
  <div class="brand"><i></i>Brightstep Learning</div>
  <h2 class="slide-title">Mom’s test &nbsp;- <span class="hl">How to do it right</span></h2>
  <p class="right-lead">You:</p>
  <ul class="checklist right-list">
    <li>Mom, when have you last time used the tablet?</li>
    <li class="plain">For what?</li>
    <li>Have you ever used it in the kitchen?</li>
    <li>Have you ever bought an app? Which? Why? For how much?</li>
    <li>Do you use your cookbooks?</li>
    <li>Is there anything you dislike about them?</li>
    <li>What was the last cookbook you bought? When? Why?</li>
  </ul>
  <div class="page-no">Page &nbsp;|&nbsp; 7</div>
</section>

<!-- ============ 8 rule of thumb ============ -->
<section class="slide col-r row-4">
  <div class="brand"><i></i>Brightstep Learning</div>
  <h2 class="slide-title">General rule of thumb to watch for</h2>
  <div class="thumb-bar" style="top:82px">
    <svg width="28" height="28" viewBox="0 0 28 28"><circle cx="14" cy="14" r="13" fill="#eef3fd"/><path d="M8,13 A6,6 0 0 1 19,10 M20,15 A6,6 0 0 1 9,18" stroke="var(--blue)" stroke-width="2.6" fill="none"/><path d="M19,6 v5 h-5z M9,22 v-5 h5z" fill="var(--blue)"/></svg>
    High frequency of usage
  </div>
  <div class="thumb-bar" style="top:148px">
    <svg width="28" height="28" viewBox="0 0 28 28"><circle cx="14" cy="14" r="13" fill="#eef3fd"/><rect x="11" y="5" width="6" height="18" rx="1.5" fill="var(--blue)"/><circle cx="14" cy="14" r="5.5" fill="#fff" stroke="var(--blue)" stroke-width="2"/><path d="M14,11 v3 h2" stroke="var(--blue)" stroke-width="1.4" fill="none"/></svg>
    It is urgent/painful enough
  </div>
  <div class="thumb-bar" style="top:211px">
    <svg width="28" height="28" viewBox="0 0 28 28"><circle cx="14" cy="14" r="13" fill="#eef3fd"/><rect x="6" y="10" width="16" height="11" rx="1.5" fill="none" stroke="var(--blue)" stroke-width="2"/><path d="M8,10 l10,-4 l2,4" stroke="var(--blue)" stroke-width="1.6" fill="none"/><circle cx="18" cy="15.5" r="1.6" fill="var(--blue)"/></svg>
    Is it worth it/ will people pay
  </div>
  <div class="page-no">Page &nbsp;|&nbsp; 8</div>
</section>

<!-- ============ 9 important questions ============ -->
<section class="slide col-l row-5">
  <div class="brand"><i></i>Brightstep Learning</div>
  <h2 class="slide-title">What to ask? Important questions</h2>
  <div class="qcard" style="left:45px;top:80px;height:185px">
    <span class="qhead good" style="left:9px;top:-2px">Good</span>
    <ul class="checklist" style="margin-top:20px">
      <li>Imagine your company failed. Why did it fail? → Questions</li>
      <li>Imagine your company is huge success why? → Questions</li>
    </ul>
    <p>Ask those questions</p>
    <p>“ you should be terrified of at least one of the questions you’re asking in every conversation”</p>
    <p>Bullet points Benefits title here</p>
  </div>
  <div class="qcard" style="left:277px;top:80px;height:185px">
    <span class="qhead" style="left:9px;top:-2px">Bad</span>
    <ul class="checklist" style="margin-top:20px">
      <li>Deep inside, you are afraid your idea might be bad</li>
      <li>So you ask bogus questions</li>
    </ul>
  </div>
  <div class="page-no">Page &nbsp;|&nbsp; 9</div>
</section>

<!-- ============ 10 mistakes: pitching ============ -->
<section class="slide col-r row-5">
  <div class="brand"><i></i>Brightstep Learning</div>
  <h2 class="slide-title">! Mistakes to avoid</h2>
  <svg class="photo" style="left:48px;top:87px" width="210" height="142" role="img" aria-label="Illustration: a cartoon salesman beside a flip chart with a speech bubble">
    <defs><linearGradient id="pitch" x1="0" y1="0" x2="1" y2="0"><stop offset="0" stop-color="#e9e9e9"/><stop offset=".5" stop-color="#b9a89a"/><stop offset="1" stop-color="#f3f1ec"/></linearGradient></defs>
    <rect width="210" height="142" fill="url(#pitch)"/>
  </svg>
  <div class="mistake-copy" style="left:293px;top:94px">
    <p class="cap" style="margin-bottom:2px">Stop pitching your product</p>
    <p><b>“Let me show you our product…”</b></p>
    <p style="margin-top:16px">You are stop learning once you get into pitch mode and failed the mom’s test.</p>
    <p><b>There is a time for it, but not when you are doing discovery customer calls</b></p>
  </div>
  <div class="page-no">Page &nbsp;|&nbsp; 10</div>
</section>

<!-- ============ 11 important questions 2 ============ -->
<section class="slide col-l row-6">
  <div class="brand"><i></i>Brightstep Learning</div>
  <h2 class="slide-title">What to ask? Important questions</h2>
  <div class="qcard" style="left:45px;top:92px;height:173px;font-size:9px;line-height:11px">
    <span class="qhead good" style="left:9px;top:-2px">Good</span>
    <ul class="checklist" style="margin-top:20px">
      <li style="margin-bottom:1px">Their life</li>
      <li style="margin-bottom:1px">Specifics in the past</li>
      <li class="sub tiny" style="margin-bottom:0">How do you solve x now?</li>
      <li class="sub tiny" style="margin-bottom:0">Why do you bother?</li>
      <li class="sub tiny" style="margin-bottom:0">What are the implications</li>
      <li class="sub tiny" style="margin-bottom:0">Talk me through the last time that happened.</li>
      <li class="sub tiny" style="margin-bottom:0">Talk me through your workflow.</li>
      <li class="sub tiny" style="margin-bottom:0">What else have you tried?</li>
      <li class="sub tiny" style="margin-bottom:2px">Where do your funds come from?</li>
      <li style="margin-bottom:1px">Who else should i talk to? &nbsp;→ expand the target group</li>
      <li>Is there anything else I should have asked? → expand knowledge</li>
    </ul>
  </div>
  <div class="qcard" style="left:277px;top:92px;height:173px;font-size:9px;line-height:11px">
    <span class="qhead" style="left:9px;top:-2px">Bad</span>
    <ul class="checklist" style="margin-top:26px">
      <li style="margin-bottom:4px">Your idea</li>
      <li style="margin-bottom:4px">Generics, Opinions</li>
      <li style="margin-bottom:2px">Would you….</li>
    </ul>
    <strong>Bad Data</strong>
    <ul class="checklist">
      <li style="margin-bottom:4px">Generics: “I always/never..”</li>
      <li style="margin-bottom:4px">Future : “ I would/ will..”</li>
      <li>Hypothetical:“ I might could..”</li>
    </ul>
  </div>
  <div class="page-no">Page &nbsp;|&nbsp; 11</div>
</section>

<!-- ============ 12 mistakes: compliments ============ -->
<section class="slide col-r row-6">
  <div class="brand"><i></i>Brightstep Learning</div>
  <h2 class="slide-title">! Mistakes to avoid</h2>
  <svg class="photo" style="left:48px;top:87px" width="210" height="142" role="img" aria-label="Photo: a torn paper note with a handwritten compliment against a blurred blue background">
    <defs><radialGradient id="note" cx="50%" cy="50%" r="65%"><stop offset="0" stop-color="#ecebe7"/><stop offset=".45" stop-color="#c9c6c0"/><stop offset="1" stop-color="#2f4f78"/></radialGradient></defs>
    <rect width="210" height="142" fill="url(#note)"/>
  </svg>
  <div class="mistake-copy" style="left:286px;top:92px;width:212px">
    <p class="cap" style="margin-bottom:8px">Empty compliments</p>
    <p style="margin-bottom:10px"><b>Don’t get flattered, it won’t help your startup</b></p>
    <p style="margin-bottom:8px">Those are warning signal during a conversation. Direct the conversation away from you and back to the customer</p>
    <p><em>“ I love this!”, “ You are such a young bright student”, “ this is a really good idea”</em></p>
  </div>
  <div class="page-no">Page &nbsp;|&nbsp; 12</div>
</section>

</body>
</html>
```